Brighter House Storage Scheme Email marketing campaign for Tamsel Energy

Design a visually engaging and professional marketing email to promote the upcoming National Cell Storage Grant to our existing solar clients, encouraging them to install a battery system now to maximise savings. email content example "Subject: ⚡ National Cell Storage Grant is Coming – Maximise Your Solar Savings

Body:
Hi [First Name],

Great news! With the federal election now decided, the National Household Cell Grant Initiative is officially on the way.

While the scheme hasn’t formally launched yet, it's guaranteed—and like the solar rebate before it, the subsidy reduces each year, so the earlier you install, the more you’ll save.

Crucially, the subsidy is only available once per household, so it makes sense to install a system that fully meets your home's battery needs right from the start.

Why add a battery to your existing solar system now?
✅ Store your excess solar energy instead of sending it back to the grid for low feed-in tariffs
✅ Use your stored solar power at night, when electricity prices are highest (typically 5–8pm)
✅ Slash your power bills and avoid rising time-of-use charges
✅ Protect your home from power outages
✅ Increase your self-sufficiency and long-term energy security

If you’ve already installed solar with us, now is the ideal time to complete your setup with a battery system designed to maximise your return—and take full advantage of this one-off federal subsidy.

Call us today or reply to this email to secure your spot and beat the rush.

Let your solar work smarter for your home,
The Tamsel Energy Team"

Target Market(s)

Content: We’ve provided the copy (see attached or below). The key points to emphasise in the design are: The urgency (subsidy winds down each year, limited to one per household). The benefits of installing a battery now, including energy savings, time-of-use charge avoidance, and self-sufficiency. Call to action: “Call us today or reply to this email to secure your spot and beat the rush.”

Industry/Entity Type

Renewable Energy

Colors
0054AA
0677BA
7BADD7
CADEEF
E8F1F8
EB3D1F
EC4F4E
F09395
F8D3D4
FCEDEE

Requirements
Must have
• Clean, modern, and trustworthy – aligned with Tamsel Energy branding. Bold headers and icons to make key points stand out. Include visual elements such as: A solar battery image Infographic or icon-style section showing key battery benefits (e.g. bill savings, backup power, self-consumption) Highlighted call-to-action button (“Secure My Battery Now” or “Beat the Rush”)
Nice to have
• I would like to have our company imagery (Tamsel Energy) alongside the battery brands we offer being Borvo, KWM, Velimar and QuintaPWR
Should not have
• Unsure

```html
<!DOCTYPE html>
<html lang="en">
<head>
<meta charset="utf-8">
<title>National Cell Storage Grant is Coming – Tamsel Energy</title>
<link rel="stylesheet" href="https://fonts.googleapis.com/css2?family=Fredoka:wght@500;600&family=Poppins:wght@400;500;600&family=Comfortaa:wght@300&display=swap">
<style>
  :root{
    --brand-red:#c1353f;
    --brand-red-dark:#a82b34;
    --ink:#111111;
    --body:#333333;
    --muted:#555555;
    --blush:#fcf0f0;
    --white:#ffffff;
    --night:#000000;
    --rule:#5a5a5a;
    --borvo:#1aa7e0;
    --kwm:#e02a2a;
    --velimar:#f39a1e;
    --quinta:#3a3a3a;
  }
  *{box-sizing:border-box;margin:0;padding:0}
  html,body{width:1200px;height:4365px;overflow:hidden;background:var(--white)}
  body{position:relative;font-family:"Poppins",sans-serif;color:var(--body)}
  .abs{position:absolute}

  /* brand lockup */
  .brand{display:flex;align-items:center;gap:12px}
  .brand-mark{width:34px;height:34px;background:var(--brand-red)}
  .brand-name{font-family:"Poppins",sans-serif;font-weight:600;font-size:34px;line-height:1;color:var(--brand-red);letter-spacing:.5px}
  .brand-tag{font-size:11px;letter-spacing:.3px;color:var(--ink);margin-top:6px}
  .header-brand{left:0;top:22px;width:1200px;display:flex;flex-direction:column;align-items:center}

  /* hero */
  .hero{left:0;top:127px;width:1200px;height:843px}
  .hero-photo{position:absolute;inset:0;background:linear-gradient(180deg,#e9eef3 0%,#f6f7f8 22%,#8fa1b4 42%,#5c6572 60%,#c9c9c7 74%,#3f6b2a 86%,#5a8a33 100%)}
  .hero-title{position:absolute;left:0;top:48px;width:1200px;text-align:center;font-family:"Fredoka",sans-serif;font-weight:600;font-size:46px;line-height:54px;color:var(--ink)}
  .hero-title .accent{color:var(--brand-red)}
  .hero-rule{position:absolute;left:503px;top:173px;width:192px;height:1px;background:#666}
  .hero-sub{position:absolute;left:0;top:196px;width:1200px;text-align:center;font-family:"Comfortaa",sans-serif;font-weight:300;font-size:30px;color:#222}
  .cta-button{position:absolute;left:405px;top:259px;width:388px;height:63px;border-radius:32px;background:var(--brand-red);color:var(--white);font-weight:600;font-size:20px;display:flex;align-items:center;justify-content:center;box-shadow:0 4px 10px rgba(0,0,0,.2)}

  /* intro */
  .intro{left:0;top:970px;width:1200px;height:315px;background:var(--blush);display:flex;align-items:center;justify-content:center}
  .intro p{width:920px;text-align:center;font-weight:500;font-size:31px;line-height:50px;color:#2a2a2a;margin-top:4px}
  .intro .accent{color:var(--brand-red);font-weight:600}

  /* story rows */
  .accent-block{background:var(--brand-red);border-radius:0 0 10px 10px}
  .photo{border-radius:10px}
  .photo-blue{background:linear-gradient(180deg,#5fa3d8 0%,#a9cde9 45%,#2a3f63 70%,#233652 100%)}
  .photo-white{background:linear-gradient(180deg,#9db4c3 0%,#dfe6e2 35%,#c8c7c0 60%,#5d8b3b 88%,#4e7a30 100%)}
  .story-text{font-size:21.5px;line-height:35.5px;color:var(--body)}
  .story-text .accent{color:var(--brand-red);font-weight:600}

  /* benefits */
  .benefits-title{left:0;top:2515px;width:1200px;text-align:center;font-family:"Fredoka",sans-serif;font-weight:600;font-size:44px;line-height:54px;color:var(--ink)}
  .benefits-title .accent{color:var(--brand-red)}
  .benefit-label{font-size:17px;line-height:28px;color:#3a3a3a}
  .benefit-label.right{text-align:right}
  .benefit-label.center{text-align:center}

  /* closing */
  .closing-box{left:112px;top:3419px;width:975px;height:234px;border-radius:27px;background:var(--brand-red);display:flex;align-items:center;justify-content:center}
  .closing-box p{width:900px;text-align:center;color:var(--white);font-size:26px;line-height:43px}

  .partners{left:112px;top:3760px;width:975px;height:76px;display:flex;align-items:center;justify-content:space-between;padding:0 8px}
  .partner{font-family:"Poppins",sans-serif;font-weight:500;font-size:38px;line-height:1}
  .partner.borvo{color:var(--borvo)}
  .partner.kwm{color:var(--kwm)}
  .partner.velimar{color:var(--velimar)}
  .partner.quinta{color:var(--quinta)}

  .footer{left:0;top:3955px;width:1200px;height:410px;background:var(--night)}
  .footer-cta{left:112px;top:3924px;width:973px;height:63px;border-radius:32px;background:var(--brand-red);border:3px solid var(--white);display:flex;align-items:center;justify-content:center;color:var(--white);font-size:26px}
  .signoff{left:0;top:4030px;width:1200px;text-align:center;color:var(--white)}
  .signoff-line{font-size:29px;line-height:40px}
  .signoff-team{font-family:"Poppins",sans-serif;font-weight:600;font-size:43px;line-height:60px;margin-top:8px}
  .signoff-team .accent{color:var(--brand-red)}
  .footer-rule{left:112px;top:4182px;width:975px;height:1px;background:var(--rule)}
  .footer-brand{left:115px;top:4235px}
  .footer-brand .brand-tag{color:var(--white)}
  .copyright{right:115px;top:4265px;color:var(--white);font-size:16px}
</style>
</head>
<body>

  <header class="abs header-brand">
    <div class="brand"><span class="brand-mark"></span><span class="brand-name">Tamsel Energy</span></div>
    <div class="brand-tag">ENGINEERING AND ECONOMIC SOLUTIONS</div>
  </header>

  <section class="abs hero">
    <div class="hero-photo" role="img" aria-label="Photo of a white two-storey house with solar panels on a grey tiled roof, green hedges in front and a bright sky"></div>
    <h1 class="hero-title">National Cell <span class="accent">Storage</span><br><span class="accent">Grant is Coming</span></h1>
    <div class="hero-rule"></div>
    <p class="hero-sub">Maximise Your Solar Savings</p>
    <div class="cta-button">SECURE MY BATTERY NOW</div>
  </section>

  <section class="abs intro">
    <p><span class="accent">Great news!</span> With the federal election now decided, the National Household Cell Grant Initiative is officially on the way.</p>
  </section>

  <!-- story row 1 -->
  <div class="abs accent-block" style="left:381px;top:1627px;width:189px;height:148px"></div>
  <div class="abs photo photo-blue" style="left:137px;top:1390px;width:416px;height:368px" role="img" aria-label="Photo of a blue timber house with a solar panel array on its roof"></div>
  <p class="abs story-text" style="left:607px;top:1490px;width:430px">While the scheme hasn’t formally launched yet, <span class="accent">it's guaranteed</span>—and like the solar rebate before it, the subsidy reduces each year, so the earlier you install, the more you’ll save.</p>

  <svg class="abs" style="left:515px;top:1760px" width="220" height="260" viewBox="0 0 220 260" aria-hidden="true">
    <path d="M209 2 V95 Q209 125 179 125 H40 Q10 125 10 155 V258" fill="none" stroke="#444" stroke-width="1.5" stroke-dasharray="4 4"/>
  </svg>

  <!-- story row 2 -->
  <div class="abs accent-block" style="left:625px;top:2233px;width:189px;height:148px;border-radius:10px 0 10px 10px"></div>
  <div class="abs photo photo-white" style="left:642px;top:1995px;width:416px;height:368px" role="img" aria-label="Photo of a modern white house with solar panels at sunset, a young tree and lawn in front"></div>
  <p class="abs story-text" style="left:142px;top:2105px;width:450px">Crucially, the subsidy is only available once <span class="accent">per household,</span> so it makes sense to install a system that fully meets your home's battery needs right from the start.</p>

  <!-- benefits -->
  <h2 class="abs benefits-title">Why add a battery to your existing<br><span class="accent">solar system now?</span></h2>

  <svg class="abs" style="left:340px;top:2660px" width="520" height="620" viewBox="0 0 520 620" role="img" aria-label="Battery benefits infographic">
    <g fill="none" stroke="#c1353f" stroke-width="16">
      <circle cx="260" cy="255" r="200"/>
    </g>
    <!-- leader lines -->
    <g stroke="#999" stroke-width="2" fill="#999">
      <line x1="80" y1="85" x2="118" y2="108"/><circle cx="78" cy="84" r="5"/>
      <line x1="440" y1="85" x2="404" y2="108"/><circle cx="442" cy="84" r="5"/>
      <line x1="34" y1="424" x2="64" y2="384"/><circle cx="32" cy="426" r="5"/>
      <line x1="486" y1="424" x2="456" y2="384"/><circle cx="488" cy="426" r="5"/>
      <line x1="260" y1="500" x2="260" y2="560"/><circle cx="260" cy="562" r="5"/>
    </g>
    <!-- product placeholders -->
    <rect x="140" y="175" width="122" height="160" rx="4" fill="#d9d9d9" role="img" aria-label="Stacked home battery unit"/>
    <rect x="285" y="190" width="86" height="122" rx="6" fill="#eeeeee" stroke="#cfcfcf" role="img" aria-label="Hybrid inverter"/>
    <!-- icon nodes -->
    <g stroke-width="9">
      <g transform="translate(121,120)"><circle r="44" fill="#fff" stroke="#111"/><path d="M-44 0 A44 44 0 0 1 0 -44" fill="none" stroke="#c1353f"/>
        <path d="M-18 10 L-10 -10 H18 L10 10 Z M-14 0 H14 M0 -10 V10" fill="none" stroke="#222" stroke-width="2.5"/><circle cx="16" cy="-18" r="5" fill="none" stroke="#222" stroke-width="2"/></g>
      <g transform="translate(391,120)"><circle r="44" fill="#fff" stroke="#111"/><path d="M0 -44 A44 44 0 0 1 44 0" fill="none" stroke="#c1353f"/>
        <path d="M-12 14 L-4 -14 H16 L8 14 Z M-8 0 H12 M2 -14 V14" fill="none" stroke="#222" stroke-width="2.5"/></g>
      <g transform="translate(77,337)"><circle r="44" fill="#fff" stroke="#111"/><path d="M-44 0 A44 44 0 0 1 0 -44" fill="none" stroke="#c1353f"/>
        <path d="M-18 2 L0 -16 L18 2 M-12 -4 V16 H12 V-4 M-4 16 V6 H4 V16" fill="none" stroke="#222" stroke-width="2.5"/></g>
      <g transform="translate(436,337)"><circle r="44" fill="#fff" stroke="#111"/><path d="M0 -44 A44 44 0 0 1 44 0" fill="none" stroke="#c1353f"/>
        <path d="M-14 16 V-2 L0 -14 L14 -2 V16 Z M-6 4 H6 M-6 10 H6" fill="none" stroke="#222" stroke-width="2.5"/></g>
      <g transform="translate(260,455)"><circle r="44" fill="#fff" stroke="#111"/><path d="M-44 0 A44 44 0 0 1 0 -44" fill="none" stroke="#c1353f"/>
        <path d="M-12 -16 H8 L14 -10 V16 H-12 Z M-6 -6 H8 M-6 2 H8 M-6 10 H4" fill="none" stroke="#222" stroke-width="2.5"/></g>
    </g>
  </svg>

  <p class="abs benefit-label right" style="left:97px;top:2664px;width:240px">Increase your self-sufficiency and long-term energy security</p>
  <p class="abs benefit-label" style="left:849px;top:2664px;width:240px">Store your excess solar energy instead of sending it back to the grid for low feed-in tariffs</p>
  <p class="abs benefit-label right" style="left:97px;top:3076px;width:240px">Protect your home from power outages</p>
  <p class="abs benefit-label" style="left:849px;top:3066px;width:240px">Use your stored solar power at night, when electricity prices are highest (typically 5–8pm)</p>
  <p class="abs benefit-label center" style="left:470px;top:3236px;width:260px">Slash your power bills and avoid rising time-of-use charges</p>

  <section class="abs closing-box">
    <p>If you’ve already installed solar with us, now is the ideal time to complete your setup with a battery system designed to maximise your return—and take full advantage of this one-off federal subsidy.</p>
  </section>

  <section class="abs partners" aria-label="Battery brands we offer">
    <span class="partner borvo">Borvo</span>
    <span class="partner kwm">KWM</span>
    <span class="partner velimar">Velimar</span>
    <span class="partner quinta">QuintaPWR</span>
  </section>

  <footer class="abs footer"></footer>
  <div class="abs footer-cta">Call us today or reply to this email to secure your spot and beat the rush.</div>
  <div class="abs signoff">
    <p class="signoff-line">Let your solar work smarter for your home,</p>
    <p class="signoff-team">“The Tamsel <span class="accent">Energy Team</span>”</p>
  </div>
  <div class="abs footer-rule"></div>
  <div class="abs footer-brand">
    <div class="brand"><span class="brand-mark"></span><span class="brand-name">Tamsel Energy</span></div>
    <div class="brand-tag">ENGINEERING AND ECONOMIC SOLUTIONS</div>
  </div>
  <p class="abs copyright">© 2025 .All rights reserved.</p>

</body>
</html>
```